Live a healthy life. Kvel

Advertising campaign for reversing type 2 diabetes and insulin resistance. The best way to reverse type 2 diabetes or put it in remission is to prevent it from triggering. We do this by healthy food choices, no overeating and exercise. The final design should promote the aforementioned and should be able to be implemented in society, schools, churches etc. Kvel is the creator of the campaign. Youtube channel "out of the head of Kvel"

```html
<!DOCTYPE html>
<html lang="en">
<head>
<meta charset="UTF-8">
<title>Reverse Type 2 Diabetes – Kvel</title>
<link rel="stylesheet" href="https://fonts.googleapis.com/css2?family=Montserrat:ital,wght@0,400;0,700;0,800;0,900;1,900&family=Oswald:wght@500&display=swap">
<style>
  :root {
    --sky: #d7eafd;
    --sky-light: #eaf4fe;
    --sky-pale: #f3f8ff;
    --navy: #0b1f63;
    --navy-deep: #021d5e;
    --royal: #0b57c5;
    --red: #e3001f;
    --ribbon: #f04345;
    --ribbon-dark: #c91c20;
    --ice: #c6e9ff;
    --lemon: #fff36b;
    --cream: #fff8cc;
    --orange: #f7931e;
    --blue-mid: #5b9be6;
  }
  * { margin: 0; padding: 0; box-sizing: border-box; }
  html, body { width: 848px; height: 1200px; overflow: hidden; background: var(--sky); }
  .poster {
    position: relative;
    width: 848px;
    height: 1200px;
    overflow: hidden;
    background: var(--sky);
    font-family: "Montserrat", sans-serif;
  }
  .backdrop { position: absolute; inset: 0; }
  .headline {
    position: absolute;
    left: 0; top: 28px;
    width: 848px;
    text-align: center;
    color: var(--navy);
    font-size: 74px;
    line-height: 76px;
    letter-spacing: -1px;
    font-weight: 400;
  }
  .headline .line { display: block; white-space: nowrap; }
  .headline .accent { color: var(--royal); font-weight: 800; }
  .headline .strong { color: var(--navy); font-weight: 800; }
  .headline .alert { color: var(--red); font-weight: 900; font-style: italic; }
  .illustration {
    position: absolute;
    left: 70px; top: 380px;
    width: 740px; height: 440px;
    border-radius: 48% 52% 40% 44%;
    background: radial-gradient(ellipse at 50% 50%, #7fb0f2 0%, #9cc3f4 38%, #f6c36a 72%, rgba(234,244,254,0) 100%);
  }
  .ribbon { position: absolute; left: 222px; top: 792px; width: 392px; height: 80px; }
  .ribbon-label {
    position: absolute;
    left: 276px; top: 814px;
    width: 288px; height: 54px;
    display: flex; align-items: center; justify-content: center;
    color: #ffffff;
    font-family: "Oswald", sans-serif;
    font-weight: 500;
    font-size: 25px;
    letter-spacing: -0.3px;
    white-space: nowrap;
  }
  .message {
    position: absolute;
    left: 48px; top: 902px;
    color: #ffffff;
    font-size: 47px;
    line-height: 54px;
    letter-spacing: 0.5px;
  }
  .message .line { display: block; white-space: nowrap; }
  .message .intro { font-weight: 400; }
  .message .food { font-weight: 800; color: var(--ice); }
  .message .portion { font-weight: 800; color: var(--lemon); }
  .message .and { font-weight: 400; color: var(--lemon); }
  .message .move { font-weight: 800; color: var(--cream); }
  .brand {
    position: absolute;
    left: 552px; top: 990px;
    width: 270px;
    display: flex; align-items: center; justify-content: center; gap: 14px;
  }
  .brand-dot { width: 30px; height: 30px; border-radius: 50%; background: var(--orange); }
  .brand-name { color: var(--navy); font-weight: 800; font-size: 64px; letter-spacing: 1px; }
</style>
</head>
<body>
<main class="poster">
  <svg class="backdrop" width="848" height="1200" viewBox="0 0 848 1200" aria-hidden="true">
    <defs>
      <linearGradient id="panelFill" x1="0" y1="0" x2="1" y2="0.3">
        <stop offset="0" stop-color="#021d5e"/>
        <stop offset="1" stop-color="#1a4fa8"/>
      </linearGradient>
      <linearGradient id="cornerFill" x1="0" y1="0" x2="0" y2="1">
        <stop offset="0" stop-color="#7fd3fb"/>
        <stop offset="0.35" stop-color="#d5eefd"/>
        <stop offset="1" stop-color="#eef7ff"/>
      </linearGradient>
    </defs>
    <rect width="848" height="1200" fill="var(--sky)"/>
    <path d="M0 480 C180 440 330 380 470 350 C620 320 720 360 848 365 L848 820 C700 800 560 790 420 805 C260 820 120 860 0 870 Z" fill="var(--sky-light)"/>
    <path d="M0 560 C200 520 380 470 560 470 C700 470 780 490 848 500" fill="none" stroke="#cfe3f8" stroke-width="1.5"/>
    <path d="M0 840 C180 830 330 810 480 800 C640 790 760 790 848 800 L848 1200 L0 1200 Z" fill="url(#cornerFill)"/>
    <path d="M0 880 C140 872 250 868 340 866 L541 866 L541 1200 L0 1200 Z" fill="url(#panelFill)"/>
  </svg>

  <h1 class="headline">
    <span class="line">The <span class="accent">Best Way</span> to</span>
    <span class="line"><span class="accent">Reverse</span> <span class="strong">Type 2</span></span>
    <span class="line"><span class="strong">Diabetes</span> is to prevent</span>
    <span class="line">it from <span class="alert">triggering</span></span>
  </h1>

  <div class="illustration" role="img" aria-label="Illustration of a raised hand with a pricked finger surrounded by a glucose meter, insulin pen, medicine bottles, leaves and hearts"></div>

  <svg class="ribbon" viewBox="0 0 392 80" aria-hidden="true">
    <polygon points="0,64 24,40 12,14 70,22 70,76" fill="var(--ribbon-dark)"/>
    <polygon points="392,64 368,40 380,14 322,22 322,76" fill="var(--ribbon-dark)"/>
    <rect x="54" y="22" width="284" height="54" fill="var(--ribbon)"/>
  </svg>
  <div class="ribbon-label">out of the head of Kvel</div>

  <p class="message">
    <span class="line intro">We do this by</span>
    <span class="line food">healthy food</span>
    <span class="line food">choices,</span>
    <span class="line portion">no overeating</span>
    <span class="line"><span class="and">and</span> <span class="move">exercise</span></span>
  </p>

  <div class="brand">
    <span class="brand-dot"></span>
    <span class="brand-name">Kvel</span>
  </div>
</main>
</body>
</html>
```